One Page Magazine Ad for New Apartment in Calgary, AB Canada

We need a one page magazine ad for a new apartment community in Calgary, Alberta.

We pride ourselves in providing the highest level of customer service and the best amenities for our community.

COMMUNITY HIGHLIGHTS

- Brand new luxury apartment rental community in the exciting Calgary Beltline neighborhood
- 13 unique spacious floor plans fit for every lifestyle (1BR-1BATH, 2BR-1BATH & 2BR-2BATH)
- Professionally managed
- On-site staff during business hours to help you with any of your needs
- Pet-friendly community
- State of the art Fitness Facility
- 2 rooftop terraces outfitted with 8 Community Brixford BBQs
- Great area for entertaining guests and a safe spot to take your dog out for some fresh air without leaving the building
- 2 resident lounges with multimedia suite, 60-inch TVs, Zentra Duo, Silver Pin Arcade system, Poker table
- Great venues to host your next party, open 24/7 free to use and bookable by residents for free!
- Monthly resident events and parties hosted by the on-site staff
- Underground secured guest and resident parking available
- Electric Car Charging Stations
- Garbage & Recycling chutes on every floor
- Controlled Access/Building
- Gated Underground Parking Garage
- Adjacent to the Beltline neighborhood bike lane on 12th Avenue SW
- Elevators - Underground Secured Bike Storage and bike repair workstation
- On-site Maintenance
- Box Waiting Package Management System
- Additional Storage Available
- Footsteps away from the local Valemart Grocery and Valemart Wine Store
- Minutes away from the new free leash dog park Ridgewell Park

APARTMENT AMENITIES

- Gourmet Kitchen with 4 piece Stainless Steel Appliances (Stove, Fridge, Microwave and Dishwasher)
- In suite dryer and washer
- Large Closets
- Patio/Balcony
- City and mountain views
- Ceramic Tile and Laminate Hardwood Flooring
- Quartz Counter-tops
- Roller Blinds for all Windows
- Walk-in Closets

For branding style, floor plans, amenities and photos please visit our website www.stayatthefenwick.example

Target Market(s)

Young Adults and Recently Single Market

Industry/Entity Type

Real Estate

Font styles to use
Sans Serif

Colors
f37122

Requirements
Must have
• - Pictures of the community
• - Possibly use of a stock photo

```html
<!DOCTYPE html>
<html lang="en">
<head>
<meta charset="utf-8">
<title>The Fenwick – Apartment Community Ad</title>
<link href="https://fonts.googleapis.com/css2?family=Open+Sans:ital,wght@0,400;0,600;0,700;0,800;1,700;1,800&display=swap" rel="stylesheet">
<style>
  :root{
    --accent:#e4442f;
    --ink:#3a3a3a;
    --paper:#ffffff;
  }
  *{box-sizing:border-box;margin:0;padding:0}
  html,body{width:863px;height:1200px;overflow:hidden;background:var(--paper)}
  body{font-family:"Open Sans",Arial,sans-serif;color:var(--ink);position:relative}

  .hero-photo{position:absolute;left:0;top:0;width:545px;height:340px;
    background:linear-gradient(160deg,#c9d6e2 0%,#9fb2c3 35%,#6c5a55 60%,#8b2b24 80%,#3c3c40 100%)}
  .brand{position:absolute;left:0;top:0;width:230px;height:68px;background:var(--paper);
    display:flex;align-items:center;gap:10px;padding-left:18px}
  .brand-square{width:22px;height:22px;background:var(--accent)}
  .brand-name{font-weight:700;font-size:15px;letter-spacing:1.5px;color:var(--accent);text-transform:uppercase}

  .web-band{position:absolute;left:0;top:290px;width:545px;height:38px;background:var(--accent);
    display:flex;align-items:center;padding-left:40px;color:#fff;font-weight:700;font-size:20px}

  .side-panel{position:absolute;left:545px;top:0;width:318px;height:340px;background:var(--accent);
    color:#fff;padding:22px 20px 0 24px}
  .side-panel .pitch{font-weight:800;font-style:italic;font-size:19px;line-height:1.22}
  .side-panel h2{font-weight:700;font-size:12.5px;margin:16px 0 6px}
  .side-panel ul{list-style:none}
  .side-panel li{font-size:8.3px;font-weight:600;line-height:1.5;padding-left:10px;position:relative}
  .side-panel li::before{content:"";position:absolute;left:0;top:4px;width:4px;height:4px;background:#fff}

  .highlights{position:absolute;left:22px;top:352px;width:820px}
  .highlights h2{display:flex;align-items:center;gap:8px;font-size:20px;font-weight:600;color:var(--ink);letter-spacing:.5px}
  .highlights h2::before{content:"";width:6px;height:22px;background:var(--accent)}
  .highlights h2::after{content:"";flex:1;height:2px;background:var(--accent)}
  .cols{display:flex;gap:30px;margin-top:12px}
  .cols ul{list-style:none;flex:1}
  .cols li{font-size:9.6px;line-height:1.45;padding-left:13px;position:relative;margin-bottom:3px}
  .cols li::before{content:"";position:absolute;left:0;top:4px;width:5px;height:5px;background:var(--accent)}

  .gallery{position:absolute;left:18px;top:648px;width:827px;height:538px;
    display:grid;grid-template-columns:1.05fr 1fr 1.05fr;grid-template-rows:1fr 1fr 1fr;gap:8px}
  .shot{border-radius:2px}
  .s1{background:linear-gradient(135deg,#e9e7e3,#a7a29a)}
  .s2{background:linear-gradient(135deg,#bfc4c8,#5d5f60)}
  .s3{background:linear-gradient(135deg,#e6e1d8,#8e8576)}
  .s4{background:linear-gradient(135deg,#f0efec,#c3bfb7)}
  .s5{background:linear-gradient(135deg,#d6c7b0,#7a6650)}
  .s6{background:linear-gradient(135deg,#cfd7df,#6f7e8a)}
  .s7{background:linear-gradient(135deg,#3e8c96,#d9d6cf)}
  .s8{background:linear-gradient(135deg,#ece8e2,#9b9387)}
  .s9{background:linear-gradient(135deg,#d9cdbd,#5b4b3d)}
</style>
</head>
<body>
  <div class="hero-photo" role="img" aria-label="Photo of the modern apartment building exterior with red and glass facade against the sky"></div>
  <div class="brand"><span class="brand-square"></span><span class="brand-name">The Fenwick</span></div>
  <div class="web-band">www.stayatthefenwick.example</div>

  <aside class="side-panel">
    <p class="pitch">We pride ourselves in providing the highest level of customer service and the best amenities for our community.</p>
    <h2>APARTMENT AMENITIES</h2>
    <ul>
      <li>Gourmet Kitchen with 4 piece Stainless Steel Appliances (Stove, Fridge, Microwave and Dishwasher)</li>
      <li>In suite dryer and washer</li>
      <li>Large Closets</li>
      <li>Patio/Balcony</li>
      <li>City and mountain views</li>
      <li>Ceramic Tile and Laminate Hardwood Flooring</li>
      <li>Quartz Counter-tops</li>
      <li>Roller Blinds for all Windows</li>
      <li>Walk-in Closets</li>
    </ul>
  </aside>

  <section class="highlights">
    <h2>COMMUNITY HIGHLIGHTS</h2>
    <div class="cols">
      <ul>
        <li>Brand new luxury apartment rental community in the exciting Calgary Beltline neighborhood</li>
        <li>13 unique spacious floor plans fit for every lifestyle (1BR-1BATH, 2BR-1BATH &amp; 2BR-2BATH)</li>
        <li>Professionally managed</li>
        <li>On-site staff during business hours to help you with any of your needs</li>
        <li>Pet-friendly community</li>
        <li>State of the art Fitness Facility</li>
        <li>2 rooftop terraces outfitted with 8 Community Brixford BBQs</li>
        <li>Great area for entertaining guests and a safe spot to take your dog out for some fresh air without leaving the building</li>
        <li>2 resident lounges with multimedia suite, 60-inch TVs, Zentra Duo, Silver Pin Arcade system, Poker table</li>
        <li>Great venues to host your next party, open 24/7 free to use and bookable by residents for free!</li>
      </ul>
      <ul>
        <li>Monthly resident events and parties hosted by the on-site staff</li>
        <li>Underground secured guest and resident parking available</li>
        <li>Electric Car Charging Stations</li>
        <li>Garbage &amp; Recycling chutes on every floor</li>
        <li>Controlled Access/Building</li>
        <li>Gated Underground Parking Garage</li>
        <li>Adjacent to the Beltline neighborhood bike lane on 12th Avenue SW</li>
        <li>Elevators - Underground Secured Bike Storage and bike repair workstation</li>
        <li>On-site Maintenance</li>
        <li>Box Waiting Package Management System</li>
        <li>Additional Storage Available</li>
        <li>Footsteps away from the local Valemart Grocery and Valemart Wine Store</li>
        <li>Minutes away from the new free leash dog park Ridgewell Park</li>
      </ul>
    </div>
  </section>

  <div class="gallery">
    <div class="shot s1" role="img" aria-label="Bright open-plan kitchen with stainless steel appliances"></div>
    <div class="shot s2" role="img" aria-label="Resident lounge with game table"></div>
    <div class="shot s3" role="img" aria-label="Living room with large windows"></div>
    <div class="shot s4" role="img" aria-label="Modern bathroom with white fixtures"></div>
    <div class="shot s5" role="img" aria-label="Kitchen with quartz counter-tops"></div>
    <div class="shot s6" role="img" aria-label="Fitness facility with exercise machines"></div>
    <div class="shot s7" role="img" aria-label="Rooftop terrace with seating and barbecues"></div>
    <div class="shot s8" role="img" aria-label="Bright bedroom with roller blinds"></div>
    <div class="shot s9" role="img" aria-label="Bedroom with warm lighting and city view"></div>
  </div>
</body>
</html>
```